New LLC consulting company needs a business card design

I need a business card design for new company in Alexandria Virginia called TK Verdant Consulting LLC. The company is focused on consulting for defense and national security issues with expertise in nuclear and space topics. I would like to see designs that are simple and I am open to colors except for brown.

Target Market(s)

All businesses that are seeking consulting help

Industry/Entity Type

Consulting

Contact Information for Business Card

Name of company - TK Verdant Consulting LLC; name (Delia Hawke) President; email: hawkedr41@mailbox-example.net; Phone: 555-271-9043

Requirements
Must have
• The details described above
Nice to have
• I'm open to all ideas
Should not have
• No brown

```html
<!DOCTYPE html>
<html lang="en">
<head>
<meta charset="UTF-8">
<title>TK Verdant Consulting LLC – Business Card</title>
<link rel="stylesheet" href="https://fonts.googleapis.com/css2?family=Cinzel:wght@600&family=Roboto:wght@400;700&display=swap">
<style>
  :root {
    --brand-blue: #0355ac;
    --ink: #2b2b2b;
    --rule: #3a3a3a;
    --card-white: #ffffff;
    --backdrop: #eceef1;
  }
  * { margin: 0; padding: 0; box-sizing: border-box; }
  html, body {
    width: 1189px;
    height: 1200px;
    overflow: hidden;
    background: var(--backdrop);
    font-family: "Roboto", Arial, sans-serif;
  }
  .canvas { position: relative; width: 1189px; height: 1200px; }
  .card {
    position: absolute;
    left: 170px;
    width: 855px;
    height: 490px;
    border-radius: 37px;
    overflow: hidden;
  }
  .card-front { top: 106px; background: var(--card-white); box-shadow: 0 4px 14px rgba(0,0,0,.12); }
  .card-back { top: 641px; background: var(--brand-blue); box-shadow: 0 4px 14px rgba(0,0,0,.15); }

  .wordmark {
    position: absolute;
    font-family: "Cinzel", Georgia, serif;
    font-weight: 600;
    text-align: center;
    line-height: 1.1;
  }
  .card-front .wordmark {
    left: 480px; top: 92px; width: 330px;
    color: var(--brand-blue);
    font-size: 34px;
  }
  .card-back .wordmark {
    left: 0; right: 0; top: 170px;
    color: var(--card-white);
    font-size: 62px;
  }
  .wordmark span { display: block; }

  .holder-name {
    position: absolute; left: 48px; top: 303px;
    color: var(--brand-blue);
    font-weight: 700; font-size: 30px;
  }
  .holder-title {
    position: absolute; left: 48px; top: 348px;
    color: var(--ink);
    font-size: 22px;
  }
  .divider {
    position: absolute; left: 49px; top: 390px;
    width: 738px; height: 2px;
    background: var(--rule);
  }
  .contact {
    position: absolute; top: 414px;
    display: flex; align-items: center; gap: 14px;
    color: var(--ink); font-size: 23px; letter-spacing: .3px;
  }
  .contact-phone { left: 46px; }
  .contact-email { left: 501px; }
  .contact svg { fill: var(--brand-blue); flex: none; }
</style>
</head>
<body>
<div class="canvas">
  <section class="card card-front">
    <div class="wordmark"><span>TK Verdant</span><span>Consulting LLC</span></div>
    <h1 class="holder-name">Delia Hawke</h1>
    <p class="holder-title">President</p>
    <div class="divider"></div>
    <div class="contact contact-phone">
      <svg width="22" height="22" viewBox="0 0 24 24" aria-hidden="true"><path d="M6.6 10.8a15.1 15.1 0 0 0 6.6 6.6l2.2-2.2a1 1 0 0 1 1-.25 11.4 11.4 0 0 0 3.6.57 1 1 0 0 1 1 1V20a1 1 0 0 1-1 1A17 17 0 0 1 3 4a1 1 0 0 1 1-1h3.5a1 1 0 0 1 1 1c0 1.25.2 2.45.57 3.57a1 1 0 0 1-.25 1z"/></svg>
      <span>555-271-9043</span>
    </div>
    <div class="contact contact-email">
      <svg width="24" height="18" viewBox="0 0 24 18" aria-hidden="true"><path d="M0 0h24v18H0z M2 2v1l10 7 10-7V2z" fill-rule="evenodd"/></svg>
      <span>hawkedr41@mailbox-example.net</span>
    </div>
  </section>

  <section class="card card-back">
    <div class="wordmark"><span>TK Verdant</span><span>Consulting LLC</span></div>
  </section>
</div>
</body>
</html>
```